Business Card Design Project

Hi,
This is a simple contest. The logo for the back of the card is deigned. See attached files. The front of the card must have :

Directors Name: Tobias
Mob:
e-mail:
Postal Address:
Web Page Adress:

It may also add words: "Leaders in Construction Project Management Services"

Target Market(s)

Business & Home owners alike

Industry/Entity Type

Business

Requirements
Must have
• See details above and logo attached
Should not have
• Images other than logo

```html
<!DOCTYPE html>
<html lang="en">
<head>
<meta charset="utf-8">
<title>Ridgeline Projects Pacific – Business Card</title>
<link href="https://fonts.googleapis.com/css2?family=PT+Sans:ital,wght@0,400;0,700;1,400&family=Arimo&display=swap" rel="stylesheet">
<style>
  :root {
    --stage: #3a3a3b;
    --label: #e2e2e2;
    --card-white: #ffffff;
    --brand-blue: #009fe0;
    --ink: #111111;
  }
  html, body {
    margin: 0;
    padding: 0;
    overflow: hidden;
  }
  .canvas {
    position: relative;
    width: 993px;
    height: 1200px;
    background: var(--stage);
    font-family: "PT Sans", sans-serif;
    overflow: hidden;
  }
  .side-label {
    position: absolute;
    left: 93px;
    margin: 0;
    font-family: "Arimo", sans-serif;
    font-size: 21px;
    font-weight: 400;
    color: var(--label);
    line-height: 1;
  }
  .side-label--front { top: 44px; }
  .side-label--back { top: 599px; }

  .card {
    position: absolute;
    left: 98px;
    width: 812px;
    height: 471px;
    box-shadow: 0 4px 14px rgba(0,0,0,0.55);
  }
  .card--front { top: 89px; background: var(--card-white); }
  .card--back { top: 653px; background: var(--brand-blue); }

  .holder-name {
    position: absolute;
    left: 61px;
    top: 78px;
    margin: 0;
    font-size: 37px;
    font-weight: 700;
    color: var(--brand-blue);
    line-height: 1;
  }
  .holder-role {
    position: absolute;
    left: 61px;
    top: 125px;
    margin: 0;
    font-size: 27px;
    font-style: italic;
    color: var(--ink);
    line-height: 1;
  }
  .postal-address {
    position: absolute;
    left: 61px;
    top: 224px;
    margin: 0;
    font-style: normal;
    font-size: 23px;
    line-height: 32px;
    color: var(--ink);
  }
  .holder-email {
    position: absolute;
    right: 45px;
    top: 104px;
    margin: 0;
    font-family: "Arimo", sans-serif;
    font-size: 24px;
    color: var(--ink);
    line-height: 1;
  }
  .contact-lines {
    position: absolute;
    right: 45px;
    top: 224px;
    margin: 0;
    text-align: right;
    font-size: 23px;
    line-height: 32px;
    color: var(--ink);
  }
  .accent-band {
    position: absolute;
    left: 0;
    top: 358px;
    width: 100%;
    height: 43px;
    background: var(--brand-blue);
  }
  .tagline {
    position: absolute;
    left: 0;
    top: 412px;
    width: 100%;
    margin: 0;
    text-align: center;
    font-size: 25px;
    font-weight: 700;
    color: var(--brand-blue);
    line-height: 1;
  }

  .brand-lockup {
    position: absolute;
    left: 0;
    top: 170px;
    width: 100%;
    display: flex;
    justify-content: center;
    align-items: center;
    gap: 22px;
  }
  .brand-square {
    width: 88px;
    height: 88px;
    background: var(--card-white);
  }
  .brand-name {
    color: var(--card-white);
    font-weight: 700;
    line-height: 1;
  }
  .brand-name__main {
    display: block;
    font-size: 72px;
    letter-spacing: 1px;
  }
  .brand-name__sub {
    display: block;
    margin-top: 4px;
    font-size: 21px;
    letter-spacing: 7px;
  }
  .back-web {
    position: absolute;
    left: 0;
    top: 394px;
    width: 100%;
    margin: 0;
    text-align: center;
    font-size: 23px;
    color: var(--card-white);
    line-height: 1;
  }
</style>
</head>
<body>
<div class="canvas">
  <p class="side-label side-label--front">Front</p>
  <section class="card card--front">
    <h1 class="holder-name">Tobias</h1>
    <p class="holder-role">Directors</p>
    <p class="holder-email">tobias@ridgelineprojects.com</p>
    <address class="postal-address">1470 harbour road<br>West Harbour, BC<br>V7Q 3K8</address>
    <p class="contact-lines">phone: (04217) 3960418<br>www.ridgelineprojects.com</p>
    <div class="accent-band"></div>
    <p class="tagline">Leaders in Construction Project Management Services</p>
  </section>

  <p class="side-label side-label--back">Back</p>
  <section class="card card--back">
    <div class="brand-lockup">
      <div class="brand-square"></div>
      <div class="brand-name">
        <span class="brand-name__main">RIDGELINE</span>
        <span class="brand-name__sub">PROJECTS PACIFIC</span>
      </div>
    </div>
    <p class="back-web">www.ridgelineprojects.com</p>
  </section>
</div>
</body>
</html>
```